Log In Screen Design

We have an existing website (www.velmarix4.com) and have recently developed software which requires a login screen using a similar theme from the velmarix4 website. The login screen should have a username and password. The software title is Tiered Outcome Scheduling (TOS). The VELMARIX4 log should appear on the login screen and the page should look professional.
Target Market(s)
Project Management Professionals
Industry/Entity Type
Software
Requirements
Must have
- Username and password blocks
Company Logo
Company Name - VELMARIX4 Management Ltd
Software Name - Tiered Outcome Scheduling (TOS)
Similar theme (colors) to the logo and existing website

```html
<!DOCTYPE html>
<html lang="en">
<head>
<meta charset="utf-8">
<title>Tiered Outcome Scheduling (TOS) – Log In</title>
<link rel="stylesheet" href="https://fonts.googleapis.com/css2?family=Carlito:wght@400;700&family=Montserrat:wght@600&display=swap">
<style>
  :root {
    --bg-centre: #d4d4d4;
    --bg-edge: #979797;
    --card-top: #f7f7f7;
    --card-bottom: #d2d2d2;
    --card-border: #1f7fc0;
    --card-border-light: #6cc6ea;
    --band-dark: #0a5aa0;
    --band-light: #0fa3d3;
    --text-dark: #1a1a1a;
    --text-light: #ffffff;
    --brand-grey: #5a5d62;
    --field-fill: #f6f6f6;
    --field-edge: #3c3c3c;
    --button-top: #8d8d8d;
    --button-bottom: #2e2e2e;
  }
  * { box-sizing: border-box; margin: 0; padding: 0; }
  html, body { width: 1200px; height: 927px; overflow: hidden; }
  body {
    position: relative;
    background: radial-gradient(ellipse 60% 65% at 50% 50%, var(--bg-centre) 0%, var(--bg-edge) 100%);
    font-family: "Carlito", "Calibri", sans-serif;
  }
  .login-shadow {
    position: absolute;
    left: 300px; top: 790px;
    width: 612px; height: 50px;
    border-radius: 50%;
    background: radial-gradient(ellipse at center, rgba(40,40,40,.55) 0%, rgba(40,40,40,0) 70%);
  }
  .login-card {
    position: absolute;
    left: 318px; top: 164px;
    width: 576px; height: 651px;
    border-radius: 70px;
    border: 3px solid var(--card-border);
    box-shadow: inset 0 0 0 2px var(--card-border-light);
    background: linear-gradient(160deg, var(--card-top) 0%, #e9e9e9 45%, var(--card-bottom) 100%);
    overflow: hidden;
  }
  .brand {
    position: absolute;
    left: 165px; top: 42px;
    display: flex; align-items: center; gap: 12px;
  }
  .brand-dot {
    width: 52px; height: 52px; border-radius: 50%;
    background: var(--brand-grey);
  }
  .brand-name {
    font-family: "Montserrat", sans-serif;
    font-weight: 600;
    font-size: 29px;
    letter-spacing: 1px;
    color: var(--brand-grey);
  }
  .title-band {
    position: absolute;
    left: 0; top: 124px;
    width: 100%; height: 71px;
    background: linear-gradient(90deg, var(--band-dark) 0%, var(--band-light) 50%, var(--band-dark) 100%);
    box-shadow: 0 8px 10px -4px rgba(0,0,0,.45);
    display: flex; align-items: center; justify-content: center;
    color: var(--text-light);
    font-size: 30px;
  }
  .login-form { position: absolute; inset: 0; }
  .field-label {
    position: absolute;
    left: 34px;
    width: 150px;
    font-size: 21px;
    color: var(--text-dark);
  }
  .field-label.username { top: 296px; }
  .field-label.password { left: 40px; top: 391px; }
  .field-input {
    position: absolute;
    left: 221px;
    width: 320px; height: 55px;
    background: var(--field-fill);
    border: none;
    border-top: 3px solid var(--field-edge);
    border-left: 3px solid var(--field-edge);
    border-right: 2px solid #9a9a9a;
    border-bottom: 1px solid #d8d8d8;
  }
  .field-input.username { top: 284px; }
  .field-input.password { top: 378px; }
  .login-button {
    position: absolute;
    left: 190px; top: 516px;
    width: 220px; height: 70px;
    border-radius: 35px;
    border: 2px solid #f0f0f0;
    background: linear-gradient(180deg, var(--button-top) 0%, #5e5e5e 50%, var(--button-bottom) 100%);
    box-shadow: 0 3px 6px rgba(0,0,0,.3);
    color: var(--text-light);
    font-family: "Carlito", "Calibri", sans-serif;
    font-size: 29px;
  }
</style>
</head>
<body>
  <div class="login-shadow"></div>
  <main class="login-card">
    <div class="brand">
      <span class="brand-dot"></span>
      <span class="brand-name">VELMARIX4</span>
    </div>
    <h1 class="title-band" style="font-weight:400">Tiered Outcome Scheduling (TOS)</h1>
    <form class="login-form">
      <label class="field-label username" for="username">Username :</label>
      <input class="field-input username" id="username" type="text">
      <label class="field-label password" for="password">Password :</label>
      <input class="field-input password" id="password" type="password">
      <button class="login-button" type="button">Log In</button>
    </form>
  </main>
</body>
</html>
```